New webpage design for Talvora.se, participant management system informationpage.

Project Brief: New Website Design for Talvora.se (Participant Management System)
About Talvora.se:
Talvora.se is an established participant management system used by organizations and course providers in Sweden to handle event and course registrations. Our website’s primary audience is course providers, event organizers, and potential users seeking efficient management tools.
Project Goal:
We are launching a new public-facing website for Talvora.se, which will present information about our system, features, FAQ, pricing, news, testimonials, and more. The new site will be built in Umbraco CMS and should follow our visual identity as described in the attached graphic manual.
Deliverables:
We need complete, modern, and responsive page designs (desktop and mobile) for the following pages:
- Home page (landing page)
- Features page
- FAQ page
- About Us page
- Contact Us / Book a Demo page
- Pricing page
- Testimonials page
- News / Blog page
Design Guidelines:
- Please use the attached Plomvik graphic manual for guidance (Plomvik is a sister project; use the same branding).
- The Talvora.se logo is attached and must be included.
- Please use the blue color palette variant from the guide.
- Typography and graphic elements should be consistent with the manual.
- Designs must be suitable for implementation in Umbraco CMS (avoid overly complex layouts or animations that might be difficult to develop).
- All designs should be responsive and work well on desktop, tablet, and mobile.
- Final deliverables should be provided in Figma or Adobe XD (preferably Figma).
What We Like:
- Clean, modern, Scandinavian style.
- Clear navigation and strong hierarchy.
- Readable, accessible layouts.
What to Avoid:
- Overly playful or cartoonish elements.
- Too much clutter or excessive graphical elements.
- Dark color schemes (please focus on blue/light).
References:
- Our current site: https://talvora-demo.se
- Graphic manual (see attachment)
- Talvora logo (see attachment)
Additional Notes:
- The new design should improve clarity, usability, and visual appeal compared to our current site.
- Feel free to suggest visual improvements, but remain consistent with our brand guidelines.
Other font styles liked:
- Orev and Cabin. See attached font files

```html
<!DOCTYPE html>
<html lang="en">
<head>
<meta charset="utf-8">
<title>Talvora – Smart Participant Management</title>
<link rel="stylesheet" href="https://fonts.googleapis.com/css2?family=Chakra+Petch:wght@500;600;700&family=Cabin:wght@400;500;600;700&display=swap">
<style>
:root{
  --blue:#0aa3ef;
  --blue-dark:#0887d0;
  --sky:#b9e5fb;
  --sky-soft:#d7f0fd;
  --teal:#16967a;
  --pink:#e8185e;
  --pink-soft:#f6a9c3;
  --yellow:#f5b400;
  --ink:#121212;
  --muted:#5d6670;
  --line:#e3e8ec;
  --canvas:#ececec;
  --white:#fff;
}
*{box-sizing:border-box;margin:0;padding:0}
html,body{width:1200px;height:4296px;overflow:hidden}
body{position:relative;background:var(--canvas);font-family:"Cabin",sans-serif;color:var(--ink)}
.abs{position:absolute}
.page{position:absolute;left:55px;top:50px;width:1102px;height:4219px;background:var(--white);overflow:hidden}
.h-font{font-family:"Chakra Petch",sans-serif;font-weight:500}
.btn{position:absolute;display:flex;align-items:center;justify-content:center;border-radius:20px;font-size:13px;color:#fff;background:var(--teal);font-family:"Cabin",sans-serif}
/* hero */
.hero-bg{left:55px;top:50px;width:1102px;height:720px;background:linear-gradient(180deg,#a9dcfa 0%,#d6effd 45%,#fff 100%)}
.nav{left:175px;top:67px;width:860px;height:40px;background:#fff;border-radius:22px;box-shadow:0 2px 8px rgba(0,0,0,.06)}
.logo{position:absolute;font-family:"Chakra Petch",sans-serif;font-weight:500;color:var(--ink)}
.nav .logo{left:17px;top:2px;font-size:30px}
.nav-links{position:absolute;left:257px;top:13px;display:flex;gap:14px;font-size:9.5px;color:#8a929a}
.nav-links .on{color:var(--ink);font-weight:600}
.nav-user{position:absolute;left:683px;top:7px;width:26px;height:26px;border-radius:50%;background:var(--blue)}
.nav-demo{position:absolute;left:720px;top:6px;width:122px;height:28px;border-radius:16px;background:var(--blue);color:#fff;font-size:12px;display:flex;align-items:center;justify-content:center}
.eyebrow{left:194px;top:166px;font-size:17px}
.hero-title{left:192px;top:196px;font-size:50px;line-height:62px;font-weight:700;white-space:nowrap}
/* mock dashboard */
.dash{left:194px;top:284px;width:615px;height:442px;background:#fff;box-shadow:0 4px 18px rgba(0,0,0,.08);overflow:hidden}
.dash-side{position:absolute;left:0;top:20px;width:104px;height:422px;background:var(--blue);color:#fff;font-size:6px}
.dash-side .logo{left:8px;top:4px;font-size:17px;color:#fff}
.side-item{position:absolute;left:8px;width:88px;height:12px;line-height:12px}
.dash-table{position:absolute;left:110px;top:100px;width:505px;font-size:7px;color:#555}
.dash-table .row{display:grid;grid-template-columns:30px 60px 88px 48px 130px 150px;height:24px;align-items:center;border-bottom:1px solid #f0f0f0;padding-left:8px}
.dash-table .head{background:var(--blue);color:#fff;height:16px}
.reg-card{left:729px;top:339px;width:289px;height:412px;background:#fff;border:5px solid #6fc9f6;box-shadow:0 6px 20px rgba(10,163,239,.25)}
.ticket{position:absolute;left:29px;width:214px;height:38px;border-radius:4px;background:var(--blue)}
.field{position:absolute;left:23px;width:226px;height:22px;border:1px solid #ddd;font-size:8px;color:#888;padding:5px 8px}
.flabel{position:absolute;left:23px;font-size:6px;color:#999}
/* stats */
.trusted{left:0;width:1200px;top:828px;text-align:center;font-size:32px;line-height:48px}
.stat{position:absolute;top:935px;display:flex;align-items:center;gap:12px;white-space:nowrap}
.stat-num{font-family:"Chakra Petch",sans-serif;font-size:50px;line-height:60px;font-weight:700}
.stat-lbl{font-size:17px;line-height:16px}
/* headings */
.sec-title{font-family:"Chakra Petch",sans-serif;font-weight:500;font-size:33px;line-height:48px;white-space:nowrap}
.arrow-btn{width:34px;height:34px;border-radius:50%;display:flex;align-items:center;justify-content:center}
.step-card{left:194px;top:1193px;width:407px;height:264px;border-radius:8px;border:1px solid var(--line);background:#fff}
.step-blue{position:absolute;left:0;top:0;width:405px;height:230px;border-radius:8px;background:var(--blue);color:#fff}
.ph{position:absolute;border-radius:8px}
/* solve */
.solve{left:55px;top:1544px;width:1102px;height:402px;background:var(--sky)}
.mini{position:absolute;background:#fff;border-radius:6px;box-shadow:0 2px 6px rgba(0,0,0,.05)}
.mini-t{position:absolute;left:12px;top:10px;font-family:"Chakra Petch",sans-serif;font-weight:500;font-size:13px}
/* features */
.feat{left:55px;top:1946px;width:1102px;height:404px;background:var(--sky-soft)}
.feat-list{left:700px;top:2056px;list-style:none;font-size:17px;font-weight:700;letter-spacing:.2px}
.feat-list li{height:38.5px;display:flex;align-items:center;gap:12px}
.tick{width:16px;height:16px;border-radius:50%;background:var(--yellow);flex:none}
/* blog */
.post{position:absolute;display:flex;flex-direction:column}
.meta{font-size:12px;color:#555;display:flex;gap:16px;align-items:center}
.post-title{font-family:"Chakra Petch",sans-serif;font-weight:700;text-transform:uppercase;letter-spacing:.2px}
.read{font-size:11px;color:#444}
/* testimonial */
.quote-txt{left:280px;top:3212px;width:650px;text-align:center;font-style:italic;font-size:13px;line-height:25px;color:#333}
/* pricing */
.price-card{position:absolute;top:3512px;width:266px;height:328px;border-radius:4px}
.price-badge{position:absolute;left:103px;top:-25px;width:58px;height:58px;border-radius:50%;background:var(--pink);border:4px solid #fff;color:#fff;font-size:17px;font-weight:600;display:flex;align-items:center;justify-content:center}
.price-name{position:absolute;left:0;width:100%;top:50px;text-align:center;font-size:17px}
.price-items{position:absolute;left:29px;top:105px;list-style:none;font-size:10px}
.price-items li{height:32px;display:flex;align-items:center;gap:12px}
.sub-btn{position:absolute;left:66px;top:280px;width:132px;height:30px;border-radius:16px;font-size:12px;display:flex;align-items:center;justify-content:center}
/* footer */
.footer{left:55px;top:3926px;width:1102px;height:343px;background:var(--sky)}
.foot-links{left:0;width:1200px;top:4144px;display:flex;justify-content:center;gap:17px;font-size:10px;color:#777}
.foot-links .on{color:var(--ink);font-weight:600}
</style>
</head>
<body>
<div class="page"></div>

<!-- HERO -->
<div class="abs hero-bg"></div>
<nav class="abs nav">
  <div class="logo">talvora.</div>
  <div class="nav-links"><span class="on">Home</span><span>Features</span><span>FAQ</span><span>About Us</span><span>Contact Us</span><span>Pricing</span><span>Testimonials</span><span>News</span></div>
  <div class="nav-user"></div>
  <div class="nav-demo">Book A Demo</div>
</nav>
<div class="abs eyebrow h-font">Smart Participant Management for</div>
<h1 class="abs hero-title h-font" style="font-weight:700">EVENTS &amp; COURSES</h1>
<div class="btn" style="left:876px;top:217px;width:137px;height:31px">Explore Features</div>

<div class="abs dash">
  <svg class="abs" style="left:8px;top:6px" width="30" height="8"><circle cx="4" cy="4" r="3" fill="#f56"/><circle cx="13" cy="4" r="3" fill="#fb3"/><circle cx="22" cy="4" r="3" fill="#3c6"/></svg>
  <div class="dash-side">
    <div class="logo">talvora.</div>
    <div class="side-item" style="top:40px">Overview</div>
    <div class="side-item" style="top:58px">Event Setup</div>
    <div class="side-item" style="top:76px">Sessions</div>
    <div class="side-item" style="top:94px">Participants</div>
    <div class="side-item" style="top:112px">Event Content</div>
    <div class="side-item" style="top:130px;background:rgba(255,255,255,.25)">Registration</div>
    <div class="side-item" style="top:148px;padding-left:12px">Form Builder</div>
    <div class="side-item" style="top:166px;padding-left:12px">Payment Methods</div>
    <div class="side-item" style="top:184px;padding-left:12px">Ticket Types</div>
    <div class="side-item" style="top:202px;padding-left:12px">Coupon Manager</div>
    <div class="side-item" style="top:220px;padding-left:12px">Registration Code</div>
    <div class="side-item" style="top:238px;padding-left:12px">Ticket Add-ons</div>
    <div class="side-item" style="top:256px;padding-left:12px">Discount Policy</div>
    <div class="side-item" style="top:274px">Courses Content</div>
  </div>
  <div class="abs" style="left:116px;top:46px;font-size:10px;font-weight:700">Registration <span style="font-weight:400;font-size:8px">| Participants</span></div>
  <div class="abs" style="left:116px;top:74px;width:265px;height:14px;border:1px solid #ddd;font-size:6px;color:#999;padding:2px 6px">Search user</div>
  <div class="abs" style="left:532px;top:33px;width:74px;height:16px;background:var(--blue);color:#fff;font-size:7px;display:flex;align-items:center;justify-content:center">+ Add Form</div>
  <div class="dash-table">
    <div class="row head"><span>☐</span><span>Form ID</span><span>Form Title</span><span>Layout</span><span>Form Type</span><span>Form Description</span></div>
    <div class="row"><span>☐</span><span>681</span><span>Registration</span><span>1-Col</span><span>Event Registration</span><span>-</span></div>
    <div class="row"><span>☐</span><span>790</span><span>Lorem ipsum</span><span>Lorem</span><span>Survey Form</span><span>Testing</span></div>
    <div class="row"><span>☐</span><span>897</span><span>Lorem ipsum dolor</span><span>Lorem</span><span>Quiz Form</span><span>-</span></div>
    <div class="row"><span>☐</span><span>910</span><span>Lorem</span><span>Lorem</span><span>Exhibitor Registration Form</span><span>-</span></div>
    <div class="row"><span>☐</span><span>974</span><span>Lorem ipsum</span><span>Lorem</span><span>Survey Form</span><span>-</span></div>
    <div class="row"><span>☐</span><span>976</span><span>Lorem ipsum</span><span>Lorem</span><span>Quiz Form</span><span>-</span></div>
    <div class="row"><span>☐</span><span>1021</span><span>Lorem</span><span>Lorem</span><span>Survey Form</span><span>-</span></div>
    <div class="row"><span>☐</span><span>1022</span><span>Ipsum dolor sit</span><span>Lorem</span><span>Survey Form</span><span>Survey Form</span></div>
    <div class="row"><span>☐</span><span>1026</span><span>Lorem ipsum</span><span>Lorem</span><span>Survey Form</span><span>Thanks</span></div>
    <div class="row"><span>☐</span><span>897</span><span>Lorem ipsum dolor</span><span>Lorem</span><span>Quiz Form</span><span>-</span></div>
    <div class="row"><span>☐</span><span>910</span><span>Lorem</span><span>Lorem</span><span>Exhibitor Registration Form</span><span>-</span></div>
    <div class="row"><span>☐</span><span>974</span><span>Lorem ipsum</span><span>Lorem</span><span>Survey Form</span><span>-</span></div>
  </div>
</div>

<div class="abs reg-card">
  <div class="abs" style="left:0;width:100%;top:22px;text-align:center;font-size:15px;font-weight:700">Event Registration</div>
  <div class="abs" style="left:23px;top:62px;font-size:8px;font-weight:600">Select Ticket</div>
  <div class="abs" style="left:209px;top:62px;width:40px;height:9px;border-radius:3px;background:#eef3ff"></div>
  <div class="ticket" style="top:88px"><div class="abs" style="left:6px;top:5px;color:#fff;font-size:7px">Premium Attendees</div></div>
  <div class="ticket" style="top:135px"><div class="abs" style="left:6px;top:5px;color:#fff;font-size:7px">Vip Attendees</div></div>
  <div class="flabel" style="top:203px">Full Name</div>
  <div class="field" style="top:212px">Lena Holmqvist</div>
  <div class="flabel" style="top:248px">Email</div>
  <div class="field" style="top:257px">lena@example.se</div>
  <div class="flabel" style="top:293px">Country</div>
  <div class="field" style="top:302px">USA</div>
  <div class="abs" style="left:78px;top:356px;width:133px;height:28px;border-radius:14px;background:var(--blue);color:#fff;font-size:10px;font-weight:700;display:flex;align-items:center;justify-content:center">REGISTRATION</div>
</div>

<!-- TRUSTED -->
<h2 class="abs trusted h-font">Trusted By Organizations<br>And Course Providers Across Sweden.</h2>
<div class="stat" style="left:198px"><span class="stat-num" style="color:var(--yellow)">+500</span><span class="stat-lbl">Events Managed<br>Monthly</span></div>
<div class="stat" style="left:500px"><span class="stat-num" style="color:var(--pink)">99.9%</span><span class="stat-lbl">System<br>Uptime</span></div>
<div class="stat" style="left:758px"><span class="stat-num" style="color:var(--teal)">10,000+</span><span class="stat-lbl">Active<br>Users</span></div>

<!-- HOW IT WORKS -->
<h2 class="abs sec-title" style="left:194px;top:1063px">How It Works In<br>3 Simple Step</h2>
<div class="abs arrow-btn" style="left:939px;top:1093px;background:var(--pink-soft)"><svg width="12" height="8"><path d="M1 1l5 5 5-5" stroke="#fff" stroke-width="2" fill="none"/></svg></div>
<div class="abs arrow-btn" style="left:984px;top:1093px;background:var(--pink)"><svg width="12" height="8"><path d="M1 7l5-5 5 5" stroke="#fff" stroke-width="2" fill="none"/></svg></div>
<div class="abs step-card">
  <div class="step-blue">
    <div class="abs" style="left:22px;top:20px;width:54px;height:54px;border-radius:50%;background:#fff"></div>
    <svg class="abs" style="left:36px;top:33px" width="26" height="28"><rect x="3" y="3" width="16" height="22" rx="2" stroke="#222" stroke-width="2" fill="none"/><path d="M7 10h8M7 15h8M7 20h5" stroke="#222" stroke-width="2"/></svg>
    <div class="abs h-font" style="left:22px;top:112px;font-size:29px;white-space:nowrap">01) Create Your Event</div>
    <div class="abs" style="left:22px;top:162px;width:370px;font-size:10.5px;line-height:19px">lorem ipsum dolor sit amet consectetur. leo amet odio sodales eget suspendisse. vitae sed commodo cursus pretium. tempor semper vel lorem lobortis viverra enim amet. pretium curabitur massa pulvinar convallis.</div>
  </div>
</div>
<div class="ph" role="img" aria-label="Team planning an event around a table with charts" style="left:613px;top:1193px;width:407px;height:264px;background:linear-gradient(135deg,#c9b39a,#8d7d70 55%,#4a3a30)"></div>

<!-- SOLVE -->
<div class="abs solve"></div>
<h2 class="abs sec-title" style="left:194px;top:1592px;font-size:32px">Solve Registration Problems<br>With Ease, Grow Your<br>Work With Speed</h2>
<div class="btn" style="left:194px;top:1856px;width:189px;height:31px">Your Success Starts Here</div>

<div class="mini" style="left:691px;top:1602px;width:133px;height:129px">
  <div class="mini-t">Average Increase</div>
  <div class="abs" style="left:18px;top:44px;font-size:8px;color:#999;line-height:24px">60<br>30<br>10</div>
  <svg class="abs" style="left:42px;top:40px" width="84" height="80">
    <rect x="4" y="30" width="4" height="45" fill="#f6b3c9"/><rect x="18" y="15" width="4" height="60" fill="#f6b3c9"/><rect x="32" y="40" width="4" height="35" fill="#f6b3c9"/><rect x="46" y="25" width="4" height="50" fill="#f6b3c9"/><rect x="60" y="35" width="4" height="40" fill="#f6b3c9"/><rect x="74" y="5" width="4" height="70" fill="var(--pink)"/>
  </svg>
</div>
<div class="mini" style="left:846px;top:1602px;width:174px;height:210px">
  <div class="mini-t">Your Work Flow</div>
  <svg class="abs" style="left:8px;top:30px" width="160" height="175">
    <rect x="0" y="120" width="16" height="50" fill="#d6f0ea"/><rect x="24" y="105" width="16" height="65" fill="#c6ebe1"/><rect x="48" y="90" width="16" height="80" fill="#b5e3d7"/><rect x="72" y="70" width="16" height="100" fill="#a1dacb"/><rect x="96" y="45" width="16" height="125" fill="var(--teal)"/><rect x="120" y="20" width="16" height="150" fill="var(--teal)"/>
  </svg>
</div>
<div class="mini" style="left:691px;top:1746px;width:133px;height:142px">
  <div class="abs" style="left:43px;top:36px;width:48px;height:22px;border-radius:11px;background:#c9d4dc" role="img" aria-label="Small customer avatars"></div>
  <div class="abs" style="left:0;width:100%;top:76px;text-align:center;font-size:10px">32.000+Kunden</div>
  <div class="abs" style="left:0;width:100%;top:92px;text-align:center;font-size:12px"><span style="color:var(--yellow)">★</span> 4.7 Bewertung</div>
</div>
<div class="mini" style="left:846px;top:1826px;width:174px;height:62px">
  <div class="abs h-font" style="left:10px;top:14px;font-size:12px;line-height:17px">Increase<br>87%</div>
  <svg class="abs" style="left:66px;top:6px" width="104" height="48"><path d="M2 40 C20 30,30 42,45 30 S70 22,80 20 S92 8,100 4 L100 46 L2 46Z" fill="#fdf1cf"/><path d="M2 40 C20 30,30 42,45 30 S70 22,80 20 S92 8,100 4" stroke="var(--yellow)" stroke-width="2" fill="none"/></svg>
</div>

<!-- FEATURES -->
<div class="abs feat"></div>
<div class="abs" role="img" aria-label="Laptop showing the Talvora dashboard on a desk" style="left:55px;top:1946px;width:591px;height:404px;background:linear-gradient(135deg,#d9dde2,#9aa3ad 60%,#5f6770)"></div>
<h2 class="abs sec-title" style="left:700px;top:1990px">Features Highlight</h2>
<ul class="abs feat-list">
  <li><span class="tick"></span>CUSTOM REGISTRATION FORMS</li>
  <li><span class="tick"></span>AUTOMATED CONFIRMATIONS</li>
  <li><span class="tick"></span>REAL-TIME REPORTING</li>
  <li><span class="tick"></span>SECURE PAYMENT INTEGRATION</li>
  <li><span class="tick"></span>ATTENDEE LIST EXPORT</li>
</ul>
<div class="btn" style="left:700px;top:2265px;width:143px;height:31px">View All Features</div>

<!-- BLOG -->
<h2 class="abs sec-title" style="left:194px;top:2428px">Latest Blog Or News</h2>
<div class="btn" style="left:895px;top:2438px;width:125px;height:31px">Explorer More</div>
<div class="ph" role="img" aria-label="Conference stage with screens and blue lighting" style="left:194px;top:2515px;width:545px;height:397px;background:linear-gradient(180deg,#1c2b7a,#2d44c8 55%,#0c1452)"></div>
<div class="post" style="left:194px;top:2926px;width:560px;gap:4px">
  <div class="meta"><span>📅 January 22, 2025</span><span>◷ 08 min read</span></div>
  <div class="post-title" style="font-size:15px;line-height:26px">Lorem ipsum dolor sit amet consectetur. In at condimentum duis auctor lectus lorem consequat.</div>
  <div class="read" style="font-size:12px">Read More →</div>
</div>

<div class="ph" role="img" aria-label="Desk with monitor and printed charts" style="left:753px;top:2515px;width:267px;height:154px;background:linear-gradient(135deg,#eee6dc,#9cb1c4 60%,#5a6a78)"></div>
<div class="post" style="left:753px;top:2676px;width:267px;gap:3px">
  <div class="meta" style="font-size:9px"><span>📅 January 22, 2025</span><span>◷ 08 min read</span></div>
  <div class="post-title" style="font-size:12px;line-height:20px">Lorem ipsum dolor sit amet consectetur. Sagittis in luctus.</div>
  <div class="read" style="font-size:9px">Read More →</div>
</div>

<div class="ph" role="img" aria-label="People networking at an event" style="left:753px;top:2777px;width:267px;height:154px;background:linear-gradient(135deg,#e8e5df,#9d968d 55%,#3f4450)"></div>
<div class="post" style="left:753px;top:2938px;width:267px;gap:3px">
  <div class="meta" style="font-size:9px"><span>📅 January 22, 2025</span><span>◷ 08 min read</span></div>
  <div class="post-title" style="font-size:12px;line-height:20px">Lorem ipsum dolor sit amet consectetur. Sit lacus enim mi.</div>
  <div class="read" style="font-size:9px">Read More →</div>
</div>

<!-- TESTIMONIALS -->
<h2 class="abs sec-title" style="left:0;width:1200px;text-align:center;top:3095px">Customer Testimonials</h2>
<svg class="abs" style="left:290px;top:3178px" width="36" height="26"><path d="M2 2h14v12l-6 10H4l5-10H2z M20 2h14v12l-6 10h-6l5-10h-7z" fill="var(--pink)"/></svg>
<p class="abs quote-txt">Lorem ipsum dolor sit amet consectetur. Vitae erat nulla facilisi rutrum duis. Mollis est sit urna id integer faucibus orci maecenas. Lectus tincidunt vitae enim bibendum. Urna et commodo volutpat leo. Facilisis lectus tempor integer nec dui velit orci odio. Commodo pellentesque gravida dignissim imperdiet rhoncus sed semper elementum. Sed nunc mauris in nec mi dictum.</p>
<div class="abs arrow-btn" style="left:195px;top:3246px;background:var(--pink-soft)"><svg width="8" height="12"><path d="M7 1L2 6l5 5" stroke="var(--pink)" stroke-width="2" fill="none"/></svg></div>
<div class="abs arrow-btn" style="left:984px;top:3246px;background:var(--pink)"><svg width="8" height="12"><path d="M1 1l5 5-5 5" stroke="#fff" stroke-width="2" fill="none"/></svg></div>
<svg class="abs" style="left:886px;top:3322px" width="36" height="26"><path d="M34 24H20V12l6-10h6l-5 10h7z M16 24H2V12L8 2h6L9 12h7z" fill="var(--pink)"/></svg>
<div class="abs" role="img" aria-label="Customer portrait" style="left:493px;top:3330px;width:72px;height:72px;border-radius:50%;background:#cfd3d7;border:4px solid #e6e8ea"></div>
<div class="abs h-font" style="left:583px;top:3333px;font-size:16px">Lena Holmqvist</div>
<div class="abs" style="left:583px;top:3358px;font-size:12px;color:#555">Lorem Ipsum Dolor Sit</div>
<div class="abs" style="left:583px;top:3374px;font-size:20px;color:var(--yellow);letter-spacing:2px">★★★★★</div>

<!-- PRICING -->
<h2 class="abs sec-title" style="left:194px;top:3514px">Pricing Teaser</h2>
<p class="abs" style="left:194px;top:3573px;font-size:13px;line-height:21px">No hidden fees. Transparent plans<br>tailored to your organization.</p>
<div class="btn" style="left:194px;top:3808px;width:115px;height:31px">View Pricing</div>

<div class="price-card" style="left:476px;background:var(--blue);color:#fff">
  <div class="price-badge">$199</div>
  <div class="price-name">Yearly Pricing</div>
  <div class="abs" style="left:29px;top:82px;width:208px;border-top:1px dashed rgba(255,255,255,.6)"></div>
  <ul class="price-items">
    <li><span class="tick"></span>Lorem ipsum dolor sit amet</li>
    <li><span class="tick"></span>Lorem ipsum dolor sit</li>
    <li><span class="tick"></span>Lorem ipsum dolor sit amet</li>
    <li><span class="tick"></span>Lorem ipsum dolor sit</li>
    <li><span class="tick"></span>Lorem ipsum dolor sit amet</li>
  </ul>
  <div class="sub-btn" style="border:1.5px solid #fff;color:#fff">Subscribe Now</div>
</div>
<div class="price-card" style="left:754px;background:#fff;border:1px solid var(--line);box-shadow:0 2px 10px rgba(0,0,0,.05)">
  <div class="price-badge">$100</div>
  <div class="price-name">Monthly Pricing</div>
  <div class="abs" style="left:29px;top:82px;width:208px;border-top:1px dashed #bbb"></div>
  <ul class="price-items">
    <li><span class="tick"></span>Lorem ipsum dolor sit amet</li>
    <li><span class="tick"></span>Lorem ipsum dolor sit</li>
    <li><span class="tick"></span>Lorem ipsum dolor sit amet</li>
    <li><span class="tick"></span>Lorem ipsum dolor sit</li>
    <li><span class="tick"></span>Lorem ipsum dolor sit amet</li>
  </ul>
  <div class="sub-btn" style="border:1.5px solid var(--yellow);color:var(--yellow)">Subscribe Now</div>
</div>

<!-- FOOTER -->
<footer class="abs footer"></footer>
<div class="abs logo" style="left:0;width:1200px;text-align:center;top:3960px;font-size:63px">talvora.</div>
<p class="abs" style="left:310px;width:580px;top:4071px;text-align:center;font-size:10px;line-height:18px">Lorem ipsum dolor sit amet consectetur. Vitae mattis feugiat sit felis Vitae nulla morbi nulla senectus ultrices lorem tristique Mollis eu turpis molestie nisl. Diam eu vitae</p>
<div class="abs foot-links"><span class="on">Home</span><span>Features</span><span>FAQ</span><span>About Us</span><span>Contact Us</span><span>Pricing</span><span>Testimonials</span><span>News</span></div>
<div class="abs" style="left:194px;top:4224px;width:826px;border-top:1px solid #7a8a95"></div>
<div class="abs" style="left:194px;top:4234px;font-size:8px">copyright © 2025 talvora · All right reserved</div>
<div class="abs" style="left:874px;top:4234px;font-size:8px">Terms of Service</div>
<div class="abs" style="left:969px;top:4234px;font-size:8px">Privacy Policy</div>
</body>
</html>
```